Corwith Lodge website redesign

After 8 years of our current site, we're ready to upgrade our site design. We'd like to generally make it more modern and clean and build it on a CMS like joomla for easier future maintenance.

Our hotel is a family-owned bed and breakfast that competes against much larger hotel chains in Aspen with fancier rooms and larger pricetags. Our hotel is priced moderately and features tasteful, uniquely-design rooms.

We are looking for a website that will showcase the uniqueness of our rooms, the history of the Lodge, and the friendliness of our staff.

Here are some other hotel sites we like:

http://www.brackenfoldhouse.example/

http://www.tollerpeakhaus.example/

http://www.quarrowstay.example/

*********

Scope of Work - I'm looking for a design AND build. The website should be built out in Joomla as part of the final deliverable.
Updates

Current website: http://www.corwithlodge.example/

Explanation of what design + build means:

I am looking for not only the design of the site, but also for the homepage and one subpage to be built out as well. I do NOT need the entire site built - only for those two pages to be built and I will retrofit the remainder of the pages.

Target Market(s)

travellers evaluating hotels in Aspen, Colorado.

Industry/Entity Type

Hotel

Requirements
Must have
• Must, must, must be based on a joomla template. "Rotating" large main image as central position on homepage is a must (see example websites mentioned above).

Nice to have
• We have an existing online reservation system. It would be nice to evaluate placing a "widget" on the homepage that integrates to the online reservation page. Similar to that feature that the Bracken Fold website has at the foot of the main image on their homepage.

```html
<!DOCTYPE html>
<html lang="en">
<head>
<meta charset="utf-8">
<title>Corwith Lodge</title>
<link href="https://fonts.googleapis.com/css2?family=Cormorant+Garamond:wght@600;700&family=Josefin+Sans:wght@300;700&family=Alegreya+Sans:wght@400&family=Crimson+Text:wght@400&family=Handlee&display=swap" rel="stylesheet">
<style>
  :root {
    --bar: rgba(30, 30, 34, 0.93);
    --panel: rgba(34, 26, 36, 0.9);
    --welcome: rgba(60, 52, 58, 0.55);
    --gold: #f3cb05;
    --gold-soft: #e9c46a;
    --orange: #e4901a;
    --white: #ffffff;
    --pink: #d68ac8;
    --link-mauve: #b07aa6;
    --button: rgba(40, 40, 44, 0.92);
    --field: #ffffff;
    --ink: #222222;
  }
  * { box-sizing: border-box; margin: 0; padding: 0; }
  html, body { width: 1200px; height: 660px; overflow: hidden; }
  body { position: relative; font-family: "Alegreya Sans", sans-serif; color: var(--white); background: #6a6a78; }

  .hero-photo {
    position: absolute; inset: 0;
    background:
      radial-gradient(ellipse at 15% 25%, rgba(92, 140, 40, 0.7), transparent 35%),
      radial-gradient(ellipse at 85% 30%, rgba(110, 150, 40, 0.6), transparent 30%),
      linear-gradient(180deg, #6f79a8 0%, #9aa0c4 35%, #b49c7c 55%, #8a7a62 75%, #5f5646 100%);
  }

  .top-bar { position: absolute; left: 0; top: 0; width: 1200px; height: 64px; background: var(--bar); }
  .brand { position: absolute; left: 152px; top: 12px; font-family: "Cormorant Garamond", serif; font-weight: 700; font-size: 34px; color: var(--gold); line-height: 1; }
  .main-nav { position: absolute; top: 18px; left: 441px; display: flex; gap: 0; }
  .main-nav a { font-family: "Cormorant Garamond", serif; font-weight: 700; font-size: 20px; color: var(--white); text-decoration: none; line-height: 24px; height: 24px; padding: 0 7px; margin-right: 13px; }
  .main-nav a.is-active { background: var(--gold); color: #1c1c1c; padding: 0 14px; }

  .booking { position: absolute; left: 144px; top: 64px; width: 172px; height: 217px; background: var(--bar); padding: 18px 17px 0; }
  .booking h2 { font-family: "Josefin Sans", sans-serif; font-weight: 700; font-size: 15px; letter-spacing: 3px; text-align: center; margin-bottom: 10px; }
  .booking label { display: block; font-size: 12px; text-align: center; font-weight: 400; margin-bottom: 2px; }
  .field { background: var(--field); color: var(--ink); font-size: 11px; text-align: center; height: 20px; line-height: 20px; margin-bottom: 8px; }
  .counts { display: flex; justify-content: space-between; font-size: 11px; }
  .selects { display: flex; justify-content: space-between; margin: 2px 0 6px; }
  .select { width: 40px; height: 16px; background: var(--field); color: var(--ink); font-size: 11px; padding-left: 3px; position: relative; }
  .select svg { position: absolute; right: 1px; top: 1px; }
  .grid-toggle { font-size: 11px; display: flex; align-items: center; gap: 5px; }
  .grid-toggle span.box { width: 11px; height: 11px; background: #ddd; border: 1px solid #999; }
  .check-btn { margin-top: 4px; background: var(--orange); font-size: 12px; text-align: center; height: 18px; line-height: 18px; }

  .quick-links { position: absolute; left: 336px; top: 78px; list-style: none; }
  .quick-links li { font-family: "Cormorant Garamond", serif; font-weight: 700; font-size: 21px; height: 49px; text-shadow: 0 1px 3px rgba(0,0,0,0.5); }

  .offers { position: absolute; left: 795px; top: 64px; width: 273px; height: 344px; background: var(--panel); padding: 16px 15px; }
  .offers h2 { font-family: "Josefin Sans", sans-serif; font-weight: 300; font-size: 22px; margin-bottom: 16px; }
  .offer { margin-bottom: 16px; }
  .offer h3 { font-family: "Josefin Sans", sans-serif; font-weight: 300; font-size: 15px; color: var(--pink); margin-bottom: 3px; }
  .offer p { font-family: "Crimson Text", serif; font-size: 11.5px; line-height: 15.5px; }
  .offer a, .offers .all { color: var(--link-mauve); text-decoration: underline; }
  .offers .all { font-family: "Crimson Text", serif; font-size: 9px; font-style: normal; }

  .action-row { position: absolute; top: 317px; left: 145px; display: flex; gap: 14px; }
  .action { width: 206px; height: 31px; background: var(--button); display: flex; align-items: center; padding-left: 10px; font-family: "Cormorant Garamond", serif; font-weight: 700; font-size: 18px; color: var(--gold); }
  .action .mark { width: 28px; height: 10px; border-radius: 5px; background: #9a9a9a; margin-right: 11px; }

  .welcome { position: absolute; left: 137px; top: 386px; width: 653px; height: 274px; background: var(--welcome); padding: 18px 22px 0; }
  .welcome h1 { font-family: "Handlee", cursive; font-weight: 400; font-size: 29px; text-align: center; }
  .welcome hr { border: none; height: 1px; background: var(--gold-soft); width: 350px; margin: 4px auto 10px; }
  .welcome p { font-size: 16px; line-height: 19.5px; margin-bottom: 12px; }

  .faint-name { position: absolute; left: 920px; top: 592px; font-family: "Cormorant Garamond", serif; font-weight: 700; font-size: 34px; color: rgba(255, 240, 200, 0.55); }
</style>
</head>
<body>
  <div class="hero-photo" role="img" aria-label="Rotating photograph of the historic stone lodge with battlements, framed by green leaves under a soft evening sky"></div>

  <header class="top-bar">
    <div class="brand">Corwith Lodge</div>
    <nav class="main-nav">
      <a class="is-active" href="#">About</a>
      <a href="#">Rooms</a>
      <a href="#">Reservation</a>
      <a href="#">Amenities</a>
      <a href="#">Webcams</a>
      <a href="#">Contact Us</a>
    </nav>
  </header>

  <form class="booking">
    <h2>STAY WITH US</h2>
    <label>Arrival Date:</label>
    <div class="field">3 Dec 2012</div>
    <label>Departure Date:</label>
    <div class="field">4 Dec 2012</div>
    <div class="counts"><span>Adults</span><span>Children</span><span>Rooms</span></div>
    <div class="selects">
      <div class="select">2<svg width="14" height="14"><rect width="14" height="14" fill="#ddd"/><path d="M3 5h8l-4 5z" fill="#333"/></svg></div>
      <div class="select"><svg width="14" height="14"><rect width="14" height="14" fill="#ddd"/><path d="M3 5h8l-4 5z" fill="#333"/></svg></div>
      <div class="select">1<svg width="14" height="14"><rect width="14" height="14" fill="#ddd"/><path d="M3 5h8l-4 5z" fill="#333"/></svg></div>
    </div>
    <div class="grid-toggle">Show Grid <span class="box"></span></div>
    <div class="check-btn">Check Availability</div>
  </form>

  <ul class="quick-links">
    <li>» Book a Room</li>
    <li>» About The Corwith Lodge</li>
    <li>» Weddings</li>
    <li>» Gift Vouchers</li>
  </ul>

  <aside class="offers">
    <h2>SPECIAL OFFERS</h2>
    <div class="offer">
      <h3>Late Availability Rate £50 B&amp;B</h3>
      <p>Stay in one of our individually designed bedrooms and enjoy a full Devon breakfast with locally sourced ingredients in the... <a href="#">Read the Rest...</a></p>
    </div>
    <div class="offer">
      <h3>Dartmoor 2 Night Break</h3>
      <p>Amazing Value !!! Enjoy a relaxing 2 night stay at The Harrowgate for 2 guests sharing one of our cosy... <a href="#">Read the Rest...</a></p>
    </div>
    <div class="offer">
      <h3>Sunday Night Special</h3>
      <p>WOW! Sizzling Sunday Night Special in November, December &amp; January – £62.50 per person DBB! Spoil yourselves on a Sunday,... <a href="#">Read the Rest...</a></p>
    </div>
    <a class="all" href="#">See All Special Offers</a>
  </aside>

  <div class="action-row">
    <div class="action"><span class="mark" role="img" aria-label="Decorative swirl"></span>Check Availability</div>
    <div class="action"><span class="mark" role="img" aria-label="Decorative swirl"></span>Current Specials</div>
    <div class="action"><span class="mark" role="img" aria-label="Decorative swirl"></span>Special Sign Up</div>
  </div>

  <section class="welcome">
    <h1>Welcome To Corwith Lodge</h1>
    <hr>
    <p>Located in the heart of downtown Aspen, the newly renovated Corwith Lodge possesses all the charms of a vintage European Ski Lodge, while offering all of the modern conveniences one would expect with a stay in Aspen.</p>
    <p>A stay at our lodge includes free continental breakfast in our dining room, daily maid service, free wireless internet access, and a fully-equipped conference facility. Guests are also invited to relax in one of our two outdoor hot tubs or in our lounge, where a 42-inch plasma TV and fireplace make for a pleasant area to unwind.</p>
  </section>

  <div class="faint-name">Corwith Lodge</div>
</body>
</html>
```